Exceptional Corporate Business Card Design

Hello,

We need an exceptional corporate business card design based on our logo attached. We require:

1. A Variation for letterpress print
2. Standard size of business card 84mm x 55mm (Artwork 88mm x 59mm)
3. Variation for square business card 65mm x 65mm (Artwork 69mm x 69mm)
4. Variation as a one side print
5. Adobe Illustrator files

The company is in the financial industry, talvenu.com

The logo is attached as vector pdf.
regards

```html
<!DOCTYPE html>
<html lang="en">
<head>
<meta charset="utf-8">
<title>Talvenu Business Card</title>
<link href="https://fonts.googleapis.com/css2?family=Lato:wght@400;700;900&display=swap" rel="stylesheet">
<style>
  :root {
    --stage: #e9e7e3;
    --card-light: #fbfbfb;
    --card-dark: #0c0c0e;
    --brand: #4a3fa3;
    --brand-soft: #6c63c0;
    --ink: #2b2b2b;
    --muted: #6b6b6b;
    --rule: #d4d4d4;
  }
  * { box-sizing: border-box; margin: 0; padding: 0; }
  html, body { width: 1200px; height: 1023px; overflow: hidden; }
  body {
    background: var(--stage);
    font-family: "Lato", Arial, sans-serif;
    position: relative;
  }
  .card {
    position: absolute;
    width: 520px;
    height: 325px;
    border-radius: 4px;
    box-shadow: 0 10px 28px rgba(0,0,0,0.18);
    overflow: hidden;
  }
  .card-front { left: 50px; top: 349px; background: var(--card-light); }
  .card-back { left: 630px; top: 349px; background: var(--card-dark); }

  .front-divider {
    position: absolute; left: 262px; top: 30px; bottom: 30px;
    width: 1px; background: var(--rule);
  }
  .brand {
    position: absolute; display: flex; align-items: center;
    color: var(--brand); font-weight: 900; letter-spacing: 2px;
  }
  .card-front .brand { left: 30px; top: 140px; font-size: 34px; gap: 10px; }
  .brand-dot { border-radius: 50%; background: var(--brand); flex: none; }
  .card-front .brand-dot { width: 40px; height: 40px; }

  .contact { position: absolute; left: 290px; top: 46px; right: 20px; }
  .contact-name { color: var(--brand); font-weight: 700; font-size: 20px; }
  .contact-role { color: var(--muted); font-size: 13px; margin-top: 2px; }
  .contact-list { list-style: none; margin-top: 20px; }
  .contact-list li {
    display: flex; align-items: center; gap: 9px;
    font-size: 13.5px; color: var(--ink); line-height: 22px;
  }
  .contact-list svg { width: 13px; height: 13px; flex: none; }
  .contact-address { margin-top: 16px; font-size: 13.5px; color: var(--ink); line-height: 20px; }

  .card-back .brand {
    left: 0; right: 0; top: 0; bottom: 0; justify-content: center;
    font-size: 64px; gap: 18px; color: var(--brand-soft);
  }
  .card-back .brand-dot { width: 84px; height: 84px; background: var(--brand-soft); }
</style>
</head>
<body>
  <section class="card card-front" aria-label="Business card front">
    <div class="brand"><span class="brand-dot"></span><span class="brand-name">TALVENU</span></div>
    <div class="front-divider"></div>
    <div class="contact">
      <p class="contact-name">Mara Ellison</p>
      <p class="contact-role">Director</p>
      <ul class="contact-list">
        <li>
          <svg viewBox="0 0 16 16" aria-hidden="true"><path d="M3 2h3l1 3-2 1a8 8 0 0 0 5 5l1-2 3 1v3a1 1 0 0 1-1 1A12 12 0 0 1 2 3a1 1 0 0 1 1-1z" fill="#4a3fa3"/></svg>
          204 518 736
        </li>
        <li>
          <svg viewBox="0 0 16 16" aria-hidden="true"><rect x="4" y="1" width="8" height="14" rx="1.5" fill="none" stroke="#4a3fa3" stroke-width="1.6"/><circle cx="8" cy="12.5" r="0.9" fill="#4a3fa3"/></svg>
          319 642 085
        </li>
        <li>
          <svg viewBox="0 0 16 16" aria-hidden="true"><rect x="1" y="3" width="14" height="10" fill="#4a3fa3"/><path d="M1 3l7 6 7-6" fill="none" stroke="#fff" stroke-width="1.2"/></svg>
          office@talvenu.com
        </li>
        <li>
          <svg viewBox="0 0 16 16" aria-hidden="true"><circle cx="8" cy="8" r="6.5" fill="none" stroke="#4a3fa3" stroke-width="1.4"/><path d="M1.5 8h13M8 1.5c-3 3.5-3 9.5 0 13M8 1.5c3 3.5 3 9.5 0 13" fill="none" stroke="#4a3fa3" stroke-width="1.1"/></svg>
          www.talvenu.com
        </li>
      </ul>
      <p class="contact-address">14-16 Alder Lane<br>W2 3QT, London, England</p>
    </div>
  </section>

  <section class="card card-back" aria-label="Business card back">
    <div class="brand"><span class="brand-dot"></span><span class="brand-name">TALVENU</span></div>
  </section>
</body>
</html>
```